Creative Businesss Card desgin!

Create a business card for our business Gleam window cleaning!
We are open to creative ideas as long as it maintains a professional image.

Target Market(s)

Small Commercial window cleaning clients including car dealerships, strata manager, cafe

Industry/Entity Type

Window Cleaning

Contact Information for Business Card

Daniel Prescott
General Manager
Gleam Window Cleaning

daniel@gleamservices.com.au
pane-care-southbank.com.au
Ph: 1800 GET GLEAM
Mob: 0437 582 061

Colors
fbed22
0392cd

Requirements
Should not have
• Stock window cleaning/ squeegee graphics

```html
<!DOCTYPE html>
<html lang="en">
<head>
<meta charset="utf-8">
<title>Gleam Window Cleaning – Business Card</title>
<link rel="stylesheet" href="https://fonts.googleapis.com/css2?family=Montserrat:wght@400;500;700;800&display=swap">
<style>
  :root {
    --page-bg: #1c1c1c;
    --card-dark: #262626;
    --panel-blue: #3a73b3;
    --panel-blue-deep: #2f63a0;
    --accent-blue: #1e6cc2;
    --chevron-mid: #2b5d9a;
    --chevron-deep: #24507f;
    --brand-yellow: #f0e321;
    --text-light: #f2f2f2;
    --badge-white: #f5f5f5;
    --badge-ink: #111111;
  }
  * { box-sizing: border-box; margin: 0; padding: 0; }
  html, body {
    width: 1200px; height: 1200px; overflow: hidden;
    background: var(--page-bg);
    font-family: "Montserrat", Arial, sans-serif;
  }
  .card {
    position: absolute; left: 100px; top: 310px;
    width: 1000px; height: 580px;
    border-radius: 56px; overflow: hidden;
    background: var(--card-dark);
  }
  .city-panel {
    position: absolute; left: 0; top: 0; width: 430px; height: 100%;
    background: linear-gradient(160deg, var(--panel-blue) 0%, var(--panel-blue-deep) 100%);
  }
  .chevron { position: absolute; }
  .chevron--left { left: 0; top: 220px; width: 110px; height: 220px; }
  .chevron--right { right: 0; top: 160px; width: 120px; height: 200px; }
  .brand {
    position: absolute; left: 122px; top: 285px;
    color: var(--brand-yellow);
    font-weight: 800; text-transform: uppercase; line-height: 1.05;
    white-space: nowrap;
  }
  .brand__name { font-size: 64px; letter-spacing: 1px; }
  .brand__tag { font-size: 20px; letter-spacing: 0.5px; margin-top: 4px; }
  .contact-pill {
    position: absolute; left: 390px; top: 240px;
    width: 96px; height: 270px; border-radius: 48px;
    background: var(--accent-blue);
    display: flex; flex-direction: column; align-items: center;
    justify-content: space-around; padding: 22px 0;
  }
  .contact-pill::before {
    content: ""; position: absolute; inset: 0 0 50% 0;
    border-radius: 48px 48px 0 0; background: var(--chevron-deep); opacity: 0.55;
  }
  .badge {
    position: relative; width: 62px; height: 62px; border-radius: 50%;
    background: var(--badge-white); color: var(--badge-ink);
    display: flex; align-items: center; justify-content: center;
    font-weight: 800; font-size: 21px;
  }
  .person { position: absolute; left: 530px; top: 100px; }
  .person__name {
    font-size: 40px; font-weight: 700; color: var(--text-light);
    text-transform: uppercase; letter-spacing: 0.5px; white-space: nowrap;
  }
  .person__name .surname { color: var(--brand-yellow); }
  .person__role {
    font-size: 24px; font-weight: 700; color: var(--text-light);
    text-transform: uppercase; margin-top: 6px; letter-spacing: 0.5px;
  }
  .details {
    position: absolute; left: 530px; top: 320px;
    color: var(--text-light); font-size: 22px; font-weight: 400; line-height: 1.35;
    white-space: nowrap;
  }
  .details__group + .details__group { margin-top: 28px; }
</style>
</head>
<body>
  <article class="card">
    <div class="city-panel" role="img" aria-label="Blue-toned city skyline photograph"></div>

    <svg class="chevron chevron--left" viewBox="0 0 110 220" aria-hidden="true">
      <polygon points="0,0 105,110 0,220" fill="var(--accent-blue)"/>
      <polygon points="0,28 78,110 0,192" fill="var(--chevron-mid)"/>
      <polygon points="0,56 52,110 0,164" fill="var(--chevron-deep)"/>
    </svg>

    <svg class="chevron chevron--right" viewBox="0 0 120 200" aria-hidden="true">
      <polygon points="120,0 0,100 120,200" fill="var(--accent-blue)"/>
      <polygon points="120,22 26,100 120,178" fill="var(--chevron-mid)"/>
      <polygon points="120,46 55,100 120,154" fill="var(--chevron-deep)"/>
    </svg>

    <div class="brand">
      <div class="brand__name">Gleam</div>
      <div class="brand__tag">Window Cleaning</div>
    </div>

    <div class="contact-pill">
      <span class="badge">E:</span>
      <span class="badge">A:</span>
    </div>

    <header class="person">
      <h1 class="person__name">Daniel <span class="surname">Prescott</span></h1>
      <p class="person__role">General Manager</p>
    </header>

    <div class="details">
      <div class="details__group">
        <p>daniel@gleamservices.com.au</p>
        <p>pane-care-southbank.com.au</p>
      </div>
      <div class="details__group">
        <p>1800 GET GLEAM</p>
        <p>0437 582 061</p>
      </div>
    </div>
  </article>
</body>
</html>
```